Plakat für Verein
Zielgruppe
Wir möchten eine Veranstaltung für unseren Verein - Hinterkalmbacher Heimatpflegeverein machen.
Aufgabenstellung
Die Party der Golden 20er
Glanz-Glamour-Lebenslust
Tanzen wie früher - Feiern wie nie
21. März - Uhrzeit: 20.30 im Saal KM
Live mit DJaneMarlies
Dresscode: Goldene 20er - Fransen, Federn, Hosenträger, Zylinder
Farbe: Gold/Schgwarz

```html
<!DOCTYPE html>
<html lang="de">
<head>
<meta charset="utf-8">
<title>Die Party der Golden 20er</title>
<link href="https://fonts.googleapis.com/css2?family=Josefin+Sans:wght@300;400;600;700&display=swap" rel="stylesheet">
<style>
  :root {
    --ink: #ffffff;
    --night: #07090c;
    --deep: #12171c;
    --gold: #c98a3a;
    --gold-bright: #f0c777;
    --amber: #e0892e;
    --teal: #4d6f72;
    --plum: #2a2130;
  }
  * { margin: 0; padding: 0; box-sizing: border-box; }
  html, body { width: 849px; height: 1200px; overflow: hidden; background: var(--night); }
  .poster {
    position: relative;
    width: 849px;
    height: 1200px;
    overflow: hidden;
    font-family: "Josefin Sans", sans-serif;
    color: var(--ink);
  }
  .poster__scene {
    position: absolute; inset: 0;
    background:
      radial-gradient(ellipse 150px 90px at 280px 590px, rgba(240,199,119,.75), transparent 70%),
      radial-gradient(ellipse 60px 40px at 460px 725px, rgba(255,214,150,.85), transparent 75%),
      radial-gradient(ellipse 90px 70px at 235px 720px, rgba(224,137,46,.7), transparent 75%),
      radial-gradient(ellipse 70px 70px at 60px 935px, rgba(224,137,46,.65), transparent 75%),
      radial-gradient(ellipse 60px 55px at 340px 1010px, rgba(201,138,58,.55), transparent 75%),
      radial-gradient(ellipse 110px 120px at 150px 790px, rgba(42,33,48,.95), transparent 75%),
      radial-gradient(ellipse 95px 330px at 620px 800px, rgba(4,6,8,.95), transparent 85%),
      radial-gradient(ellipse 200px 140px at 260px 470px, rgba(77,111,114,.55), transparent 75%),
      radial-gradient(ellipse 200px 110px at 790px 640px, rgba(240,199,119,.35), transparent 75%),
      radial-gradient(ellipse 260px 160px at 420px 820px, rgba(77,111,114,.5), transparent 75%),
      radial-gradient(ellipse 520px 260px at 420px 1000px, rgba(201,138,58,.35), transparent 80%),
      linear-gradient(180deg, var(--night) 0%, var(--night) 30%, var(--deep) 48%, #1d2327 78%, #0c0f12 100%);
  }
  .poster__title {
    position: absolute; left: 0; right: 0; top: 38px;
    text-align: center;
    font-weight: 600;
    font-size: 94px;
    line-height: 100px;
  }
  .poster__title span { display: block; }
  .poster__tagline {
    position: absolute; left: 0; right: 0; top: 240px;
    text-align: center;
    font-weight: 300;
    font-size: 50px;
    letter-spacing: 1px;
  }
  .poster__live {
    position: absolute; left: 160px; top: 398px;
    width: 440px;
    text-align: center;
    font-weight: 400;
    font-size: 35px;
    white-space: nowrap;
    transform: rotate(19.6deg);
  }
  .host {
    position: absolute; left: 0; right: 0; top: 932px;
    text-align: center;
  }
  .host__dot {
    width: 62px; height: 62px; border-radius: 50%;
    background: var(--ink);
    margin: 0 auto 20px;
  }
  .host__name {
    font-weight: 700;
    font-size: 18.5px;
    line-height: 24px;
    text-transform: uppercase;
    letter-spacing: .5px;
  }
  .poster__motto {
    position: absolute; left: 0; right: 0; top: 1076px;
    text-align: center;
    font-weight: 400;
    font-size: 34px;
  }
  .poster__date {
    position: absolute; left: 0; right: 0; top: 1113px;
    text-align: center;
    font-weight: 700;
    font-size: 35px;
    text-transform: uppercase;
  }
  .poster__dresscode {
    position: absolute; left: 0; right: 0; top: 1157px;
    text-align: center;
    font-weight: 300;
    font-size: 24px;
  }
  .poster__credit {
    position: absolute; left: 2px; top: 1190px;
    font-size: 5px;
    opacity: .6;
    transform: rotate(-90deg);
    transform-origin: left top;
    white-space: nowrap;
  }
</style>
</head>
<body>
<main class="poster">
  <div class="poster__scene" role="img" aria-label="Festlich gedeckter Tisch bei Nacht mit Sektschale, Proseccoflasche, Weintrauben, Orangen, Kerze und goldener Lichterkette"></div>

  <h1 class="poster__title"><span>DIE PARTY DER</span><span>GOLDEN 20ER</span></h1>
  <p class="poster__tagline">Glanz - Glamour - Lebenslust</p>
  <p class="poster__live">Live mit DJane Marlies</p>

  <div class="host">
    <div class="host__dot"></div>
    <p class="host__name">Hinterkalmbacher<br>Heimatpflegeverein</p>
  </div>

  <p class="poster__motto">Tanzen wie früher - Feiern wie nie!</p>
  <p class="poster__date">21. März - Uhrzeit: 20.30 im Saal KM</p>
  <p class="poster__dresscode">Dresscode: Goldene 20er - Fransen, Federn, Hosenträger, Zylinder</p>
  <p class="poster__credit">Foto: Vereinsarchiv Kalmbach</p>
</main>
</body>
</html>
```